Pellworth and Tasker Ranch Insurance

Would like you all to design a logo for our Business cards and possible letterhead.
This business provides Ranch insurance for folks in Texas, New Mexico, and Oklahoma

Ggood stuff everybody, be sure to include email and Mobil for both of us on all designs

Thanks

Hello All

Wanted to let you all know i am going to extend deadline a few days, and add some more $$ to the budget

Reason: Give everybody a bit ,more time, and I added more money

Appreciate all of yalls hard work, will review and provide feed back hopefully today, been a little whacky with the holidays and all

Industry/Entity Type

Business

```html
<!DOCTYPE html>
<html lang="en">
<head>
<meta charset="utf-8">
<title>Pellworth and Tasker Ranch Insurance – Stationery</title>
<link rel="stylesheet" href="https://fonts.googleapis.com/css2?family=Source+Sans+3:wght@400;600&display=swap">
<style>
  :root {
    --bg: #e6e3df;
    --paper: #ffffff;
    --card: #f7f6f3;
    --brown: #3a2618;
    --ink: #2b2b2b;
    --rule: #d9d4ce;
    --font: "Source Sans 3", Arial, sans-serif;
  }
  * { box-sizing: border-box; margin: 0; padding: 0; }
  html, body { width: 1200px; height: 1157px; overflow: hidden; }
  body { background: var(--bg); font-family: var(--font); color: var(--ink); position: relative; }

  .sheet { position: absolute; background: var(--paper); box-shadow: 0 2px 8px rgba(0,0,0,.15); overflow: hidden; }
  .icon { width: 11px; height: 11px; fill: var(--ink); vertical-align: -1px; flex: none; }

  .brand { text-align: center; color: var(--brown); font-weight: 600; line-height: 1.05; }
  .brand .brand-name { display: block; }
  .brand .brand-sub { display: block; border-top: 1px solid var(--brown); margin-top: 3px; padding-top: 2px; }

  /* Business card front */
  .card-front { left: 30px; top: 151px; width: 450px; height: 257px; border-radius: 16px; background: var(--card); }
  .card-front .brand { position: absolute; left: 100px; top: 48px; width: 250px; }
  .card-front .brand-name { font-size: 24px; }
  .card-front .brand-sub { font-size: 12px; width: 150px; margin: 4px auto 0; }
  .contact { position: absolute; font-size: 13px; line-height: 1.35; white-space: nowrap; }
  .contact .person { font-size: 17px; border-bottom: 1px solid var(--ink); padding-bottom: 2px; margin-bottom: 4px; }
  .contact .line { display: flex; align-items: center; gap: 6px; }
  .card-front .left { left: 26px; top: 150px; width: 200px; }
  .card-front .right { right: 26px; top: 118px; width: 200px; text-align: right; }
  .card-front .right .line { justify-content: flex-end; }
  .card-band { position: absolute; left: 0; right: 0; bottom: 0; height: 38px; background: var(--brown); color: #fff; font-size: 13px; display: flex; justify-content: space-between; align-items: center; padding: 0 26px; white-space: nowrap; }
  .card-band .line { display: flex; align-items: center; gap: 6px; }
  .card-band .icon { fill: #fff; }

  /* Business card back */
  .card-back { left: 30px; top: 433px; width: 450px; height: 257px; border-radius: 16px; background: var(--card); }
  .card-back .brand { position: absolute; left: 100px; top: 82px; width: 250px; }
  .card-back .brand-name { font-size: 24px; }
  .card-back .brand-sub { font-size: 12px; width: 150px; margin: 4px auto 0; }
  .web { display: flex; align-items: center; justify-content: center; gap: 5px; font-size: 12px; white-space: nowrap; }
  .card-back .web { position: absolute; left: 0; right: 0; bottom: 28px; }

  /* Envelope */
  .envelope { left: 30px; top: 715px; width: 450px; height: 196px; }
  .envelope .brand { position: absolute; left: 18px; top: 22px; width: 140px; }
  .envelope .brand-name { font-size: 14px; }
  .envelope .brand-sub { font-size: 8px; width: 90px; margin: 3px auto 0; }
  .envelope .web { position: absolute; left: 0; right: 0; bottom: 20px; font-size: 9px; }
  .envelope .web .icon { width: 8px; height: 8px; }
  .envelope-band { position: absolute; left: 0; right: 0; bottom: 0; height: 14px; background: var(--brown); }

  /* Letterhead */
  .letterhead { left: 510px; top: 151px; width: 660px; height: 854px; border-radius: 12px; }
  .letterhead .brand { position: absolute; left: 28px; top: 52px; width: 170px; }
  .letterhead .brand-name { font-size: 18px; }
  .letterhead .brand-sub { font-size: 9px; width: 110px; margin: 3px auto 0; }
  .letterhead .contact { font-size: 10px; line-height: 1.35; }
  .letterhead .contact .person { font-size: 13px; border: 0; margin-bottom: 3px; padding: 0; }
  .letterhead .contact .line { gap: 5px; }
  .letterhead .icon { width: 9px; height: 9px; }
  .lh-dale { left: 350px; top: 38px; }
  .lh-ray { left: 486px; top: 38px; }
  .lh-office { position: absolute; left: 350px; top: 96px; display: flex; gap: 0; font-size: 10px; white-space: nowrap; }
  .lh-office .line { display: flex; align-items: center; gap: 5px; }
  .lh-office .line:first-child { width: 136px; }
  .lh-rule { position: absolute; left: 20px; right: 20px; top: 122px; border-top: 1px solid var(--rule); }
  .lh-band { position: absolute; left: 0; right: 0; bottom: 0; height: 26px; background: var(--brown); color: #fff; font-size: 10px; }
  .lh-band .web { height: 100%; }
  .lh-band .icon { fill: #fff; }
</style>
</head>
<body>
<svg width="0" height="0" style="position:absolute" aria-hidden="true">
  <symbol id="i-mobile" viewBox="0 0 12 12"><path d="M3 0h6a1 1 0 0 1 1 1v10a1 1 0 0 1-1 1H3a1 1 0 0 1-1-1V1a1 1 0 0 1 1-1zm0 1.5v7.5h6V1.5z"/></symbol>
  <symbol id="i-mail" viewBox="0 0 12 12"><path d="M0 2h12v8H0zm1.2 1L6 6.4 10.8 3zm-.2 1.2V9h10V4.2L6 7.6z"/></symbol>
  <symbol id="i-phone" viewBox="0 0 12 12"><path d="M1 4c0-2 2.5-2.5 5-2.5S11 2 11 4l-2 .6-.5-1.4h-5L3 4.6zM3 5.5h6l1.5 5h-9z"/></symbol>
  <symbol id="i-pin" viewBox="0 0 12 12"><path d="M6 0a4 4 0 0 1 4 4c0 3-4 8-4 8S2 7 2 4a4 4 0 0 1 4-4zm0 2.3A1.7 1.7 0 1 0 6 5.7 1.7 1.7 0 0 0 6 2.3z"/></symbol>
  <symbol id="i-search" viewBox="0 0 12 12"><path d="M7 0a5 5 0 1 1-2.9 9.1L1.4 11.8 0.2 10.6 2.9 7.9A5 5 0 0 1 7 0zm0 1.6A3.4 3.4 0 1 0 7 8.4 3.4 3.4 0 0 0 7 1.6z"/></symbol>
</svg>

<section class="sheet card-front" aria-label="Business card front">
  <div class="brand"><span class="brand-name">Pellworth and Tasker</span><span class="brand-sub">Ranch Insurance</span></div>
  <div class="contact right">
    <div class="person">Dale Pellworth</div>
    <div class="line">512-555-0187 <svg class="icon"><use href="#i-mobile"/></svg></div>
    <div class="line">pellworthd@ranchco.com <svg class="icon"><use href="#i-mail"/></svg></div>
  </div>
  <div class="contact left">
    <div class="person">T. Ray Tasker</div>
    <div class="line"><svg class="icon"><use href="#i-mobile"/></svg> 325-555-0146</div>
    <div class="line"><svg class="icon"><use href="#i-mail"/></svg> ray@pellworthandtasker.com</div>
  </div>
  <div class="card-band">
    <span class="line"><svg class="icon"><use href="#i-phone"/></svg> 325.555.0120</span>
    <span class="line">408 W Oak St, Marfa, TX 79843 <svg class="icon"><use href="#i-pin"/></svg></span>
  </div>
</section>

<section class="sheet card-back" aria-label="Business card back">
  <div class="brand"><span class="brand-name">Pellworth and Tasker</span><span class="brand-sub">Ranch Insurance</span></div>
  <div class="web"><svg class="icon"><use href="#i-search"/></svg> http://www.pellworthandtasker.com</div>
</section>

<section class="sheet envelope" aria-label="Envelope">
  <div class="brand"><span class="brand-name">Pellworth and Tasker</span><span class="brand-sub">Ranch Insurance</span></div>
  <div class="web"><svg class="icon"><use href="#i-search"/></svg> http://www.pellworthandtasker.com</div>
  <div class="envelope-band"></div>
</section>

<section class="sheet letterhead" aria-label="Letterhead">
  <div class="brand"><span class="brand-name">Pellworth and Tasker</span><span class="brand-sub">Ranch Insurance</span></div>
  <div class="contact lh-dale">
    <div class="person">Dale Pellworth</div>
    <div class="line"><svg class="icon"><use href="#i-mobile"/></svg> 512-555-0187</div>
    <div class="line"><svg class="icon"><use href="#i-mail"/></svg> pellworthd@ranchco.com</div>
  </div>
  <div class="contact lh-ray">
    <div class="person">T. Ray Tasker</div>
    <div class="line"><svg class="icon"><use href="#i-mobile"/></svg> 325-555-0146</div>
    <div class="line"><svg class="icon"><use href="#i-mail"/></svg> ray@pellworthandtasker.com</div>
  </div>
  <div class="lh-office">
    <span class="line"><svg class="icon"><use href="#i-phone"/></svg> 325.555.0120</span>
    <span class="line"><svg class="icon"><use href="#i-pin"/></svg> 408 W Oak St, Marfa, TX 79843</span>
  </div>
  <div class="lh-rule"></div>
  <div class="lh-band"><div class="web"><svg class="icon"><use href="#i-search"/></svg> http://www.pellworthandtasker.com</div></div>
</section>
</body>
</html>
```